Corporate Wall Mural for Office

We have several offices across North America and we want to have a corporate wall mural in each office, so we require a mural wall design that can be adjusted for different wall dimensions and still look good.

The first mural will be 239.5" x 112.5" it will be in our Toronto office - so the background city will be the Toronto skyline

I have attached a draft design and the content PNG file.

We want a different design that keeps the content outlined in the Mural Design Content PNG file.

Our corporate font is Gilroy Semi Bold

Our corporate colors are
Blue
C94
M70
Y0
K12
Pantone 2945C

Purple
C 80
M 78
PMS 2368 C

Sky Blue
C68
M34
PMS 2727 C
Our website is qalverpoint.com

Founded in 2012, QPT is a leading provider of technology infrastructure solutions, specializing in Broadband, DAS/Private Networks, Fixed Wireless Access, Site Solutions, Carrier Networks, and Test & Measurement. Our mission is to empower organizations of all sizes with innovative connectivity and telecom infrastructure solutions to build the future of communications.

Target Market(s)

Target is the staff and visitors of our office

Industry/Entity Type

network infrastructure: both wireless and wireline

Font styles to use
Sans Serif
Other font styles liked:
• Gilroy Semi-Bold and Bold

Colors
0054AA
0677BA
7BADD7
CADEEF
E8F1F8

Requirements
Must have
• the info listed in the Mural Content.png file, our corporate colors. It should be bright and energetic.
Nice to have
• I like concept of the city silhouette from the draft design

```html
<!DOCTYPE html>
<html lang="en">
<head>
<meta charset="utf-8">
<title>QPT Office Mural</title>
<link href="https://fonts.googleapis.com/css2?family=Outfit:wght@400;500;600;700&display=swap" rel="stylesheet">
<style>
  :root {
    --royal: #0a22d4;
    --brand-blue: #1a4fd8;
    --skyline: #1548e0;
    --sky-light: #2a7cf0;
    --teal: #1c8a7a;
    --cyan: #4fc8f2;
    --card: #f4f6f8;
    --ink: #161616;
    --white: #ffffff;
  }
  * { margin: 0; padding: 0; box-sizing: border-box; }
  html, body { width: 1200px; height: 564px; overflow: hidden; background: var(--white); }
  .mural {
    position: relative; width: 1200px; height: 564px; overflow: hidden;
    font-family: "Outfit", sans-serif; font-weight: 500; background: var(--white);
  }
  .layer { position: absolute; left: 0; top: 0; }

  .brand { position: absolute; left: 26px; top: 28px; display: flex; align-items: center; gap: 12px; }
  .brand-dot { width: 62px; height: 62px; border-radius: 50%; background: var(--brand-blue); }
  .brand-name { font-size: 46px; font-weight: 700; color: var(--ink); letter-spacing: 1px; line-height: 1; }

  .unique { position: absolute; left: 36px; top: 176px; color: var(--white); }
  .unique h2 { font-size: 15px; font-weight: 500; margin-bottom: 17px; }
  .unique p { margin-left: 21px; font-size: 13.5px; line-height: 18px; margin-bottom: 8px; width: 282px; }
  .unique .label { color: var(--cyan); }

  .values-title { position: absolute; left: 36px; top: 371px; color: var(--white); font-size: 15px; font-weight: 500; }
  .value { position: absolute; width: 70px; text-align: center; color: var(--white); font-size: 7.5px; line-height: 9px; }
  .value .photo {
    width: 40px; height: 40px; border-radius: 50%; margin: 0 auto 3px;
    background: radial-gradient(circle at 40% 35%, #c9b8a6, #5d6f86);
    border: 1.5px solid var(--white);
  }

  .headline {
    position: absolute; left: 579px; top: 30px; color: var(--brand-blue);
    font-size: 23.6px; font-weight: 700; white-space: nowrap;
  }
  .tagline {
    position: absolute; left: 508px; top: 95px; color: var(--brand-blue);
    font-size: 15.2px; font-weight: 600; white-space: nowrap;
  }

  .card {
    position: absolute; top: 148px; width: 156px; height: 188px; background: var(--card);
    padding-top: 17px; color: var(--brand-blue);
    box-shadow: 0 6px 6px -3px rgba(0,0,0,0.35);
  }
  .card h3 { text-align: center; font-size: 15.5px; font-weight: 500; }
  .card h3::after {
    content: ""; display: block; width: 86px; height: 1.5px; background: var(--brand-blue);
    margin: 5px auto 0;
  }
  .card ul { list-style: none; margin-top: 20px; padding-left: 20px; }
  .card li { font-size: 10.5px; line-height: 15.6px; position: relative; padding-left: 11px; }
  .card li::before { content: "•"; position: absolute; left: 0; }
  .card.markets ul { margin-top: 14px; }
  .capabilities { left: 576px; }
  .services { left: 770px; }
  .markets { left: 964px; }
</style>
</head>
<body>
<div class="mural">
  <svg class="layer city-skyline" width="1200" height="564" viewBox="0 0 1200 564" role="img" aria-label="Toronto city skyline silhouette in brand blue">
    <defs>
      <linearGradient id="skylineTone" x1="0" y1="0" x2="0" y2="1">
        <stop offset="0" stop-color="#ffffff"/>
        <stop offset="0.35" stop-color="#c9d8f8"/>
        <stop offset="0.6" stop-color="#3f72ea"/>
        <stop offset="1" stop-color="#1444dc"/>
      </linearGradient>
    </defs>
    <rect x="330" y="190" width="870" height="322" fill="url(#skylineTone)"/>
  </svg>

  <svg class="layer" width="1200" height="564" viewBox="0 0 1200 564" aria-hidden="true">
    <rect x="0" y="528" width="1200" height="36" fill="var(--skyline)"/>
    <rect x="300" y="512" width="725" height="16" fill="#f4f6f8"/>
    <polygon points="1006,495 1200,495 1200,528 1024,528" fill="var(--sky-light)"/>
    <polygon points="503,76 1025,76 1015,92 503,92" fill="var(--teal)"/>
    <polygon points="1025,76 1200,76 1200,110 1010,110 1000,94" fill="var(--brand-blue)"/>
    <polygon points="0,0 530,0 283,564 0,564" fill="var(--royal)"/>
    <polygon points="528,0 542,0 296,564 280,564" fill="var(--teal)"/>
    <path d="M0,0 H305 C270,62 215,112 150,124 C95,134 40,130 0,134 Z" fill="var(--white)" stroke="var(--teal)" stroke-width="4"/>
  </svg>

  <div class="brand">
    <span class="brand-dot"></span>
    <span class="brand-name">QPT</span>
  </div>

  <section class="unique">
    <h2>WHAT MAKES US UNIQUE?</h2>
    <p><span class="label">QPT Touch:</span> We are more than a catalog</p>
    <p><span class="label">QPT Experience:</span> A pleasure to do business with. Proactive, Professional and Precise</p>
    <p><span class="label">QPT Solution:</span> Design, Develop, and Deliver. Custom Solutions; On-Time and On-Spec</p>
  </section>

  <h2 class="values-title">Our Core Values</h2>
  <div class="value" style="left:47px;top:418px;"><div class="photo" role="img" aria-label="Team members working together at a desk"></div>People First</div>
  <div class="value" style="left:109px;top:418px;"><div class="photo" role="img" aria-label="Colleague reviewing work on a laptop"></div>Intellectual Curiosity</div>
  <div class="value" style="left:177px;top:418px;"><div class="photo" role="img" aria-label="Employee at a computer workstation"></div>Continuous Improvement</div>
  <div class="value" style="left:47px;top:478px;"><div class="photo" role="img" aria-label="Team meeting with a client"></div>Customer Focus</div>
  <div class="value" style="left:109px;top:478px;"><div class="photo" role="img" aria-label="Staff collaborating in a bright office"></div>Results Matter</div>

  <h1 class="headline">ENABLING SOLUTIONS FOR A CONNECTED WORLD</h1>
  <p class="tagline">We Distribute Products and Solution Services for Digital Infrastructure</p>

  <section class="card capabilities">
    <h3>Our Capabilities</h3>
    <ul>
      <li>Wireless Infrastructure</li>
      <li>Broadband &amp; Fiber</li>
      <li>Site Solutions</li>
      <li>Fixed Wireless Access</li>
      <li>Test &amp; Measurement</li>
      <li>DAS &amp; PWN</li>
      <li>Power Solutions</li>
    </ul>
  </section>
  <section class="card services">
    <h3>Solutions Services</h3>
    <ul>
      <li>Kitting &amp; Logistics</li>
      <li>Professional Engineering</li>
      <li>Placeholder</li>
      <li>Placeholder</li>
      <li>Placeholder</li>
    </ul>
  </section>
  <section class="card markets">
    <h3>Our Markets</h3>
    <ul>
      <li>Carriers &amp; Cable Companies</li>
      <li>Data Centers</li>
      <li>Utilities</li>
      <li>Federal Government</li>
      <li>Education</li>
      <li>Industrial Manufacturing &amp; Digital Supply Chain</li>
    </ul>
  </section>
</div>
</body>
</html>
```